Presentation Folder Design - (Pocket Folder)

We are an accounting firm for dentists. We need a folder designed for our marketing material. Attached is our logo.

Accounting

```html
<!DOCTYPE html>
<html lang="en">
<head>
<meta charset="utf-8">
<title>Larkfield Ledger Partners – Pocket Folder</title>
<link rel="stylesheet" href="https://fonts.googleapis.com/css2?family=Roboto:wght@400;700&display=swap">
<style>
  :root {
    --stage: #e6e7e9;
    --slate: #36464f;
    --slate-deep: #2b3842;
    --brand-blue: #2a9fd8;
    --paper: #ffffff;
    --paper-shade: #eceef0;
    --photo-skin: #e8c8b6;
    --contact-text: #9aa6af;
  }
  * { box-sizing: border-box; margin: 0; padding: 0; }
  html, body { width: 1200px; height: 847px; overflow: hidden; }
  body {
    background: var(--stage);
    font-family: "Roboto", Arial, sans-serif;
    position: relative;
  }
  .folder-spread {
    position: absolute;
    left: 120px;
    top: 103px;
    width: 960px;
    height: 640px;
    display: flex;
    box-shadow: 0 14px 40px rgba(0,0,0,0.18);
  }
  .panel {
    position: relative;
    width: 480px;
    height: 640px;
    overflow: hidden;
    background: linear-gradient(160deg, var(--slate), var(--slate-deep));
  }
  .panel svg.panel-art { position: absolute; inset: 0; }
  .firm-name {
    position: absolute;
    color: var(--brand-blue);
    font-weight: 700;
    font-size: 24px;
    letter-spacing: -0.2px;
    white-space: nowrap;
  }
  .back-cover .firm-name { left: 56px; top: 462px; }
  .front-cover .firm-name { left: 0; right: 0; top: 112px; text-align: center; }
  .contact-list {
    position: absolute;
    left: 58px;
    top: 522px;
    list-style: none;
    color: var(--contact-text);
    font-size: 10px;
    letter-spacing: 1.6px;
  }
  .contact-list li { display: flex; align-items: center; gap: 10px; height: 15px; }
  .contact-list svg { width: 10px; height: 10px; flex: none; }
</style>
</head>
<body>
  <main class="folder-spread">
    <section class="panel back-cover">
      <svg class="panel-art" width="480" height="640" viewBox="0 0 480 640">
        <defs>
          <linearGradient id="photoTone" x1="0" y1="0" x2="1" y2="1">
            <stop offset="0" stop-color="#f4e6df"/>
            <stop offset="0.55" stop-color="var(--photo-skin)"/>
            <stop offset="1" stop-color="#f1f2f3"/>
          </linearGradient>
        </defs>
        <path d="M0 0 H480 V215 Q250 300 0 300 Z" fill="var(--paper-shade)"/>
        <path d="M0 0 H370 Q300 250 0 290 Z" fill="url(#photoTone)"
              role="img" aria-label="Photo of a smiling woman holding a green apple to her cheek"/>
        <path d="M370 0 Q300 250 0 290" fill="none" stroke="var(--brand-blue)" stroke-width="5"/>
        <path d="M480 215 Q250 300 0 300" fill="none" stroke="var(--brand-blue)" stroke-width="2"/>
      </svg>
      <span class="firm-name">Larkfield Ledger Partners</span>
      <ul class="contact-list">
        <li><svg viewBox="0 0 10 10"><path d="M2 1 L4 1 L4.6 3 L3.5 3.8 Q4.5 5.8 6.2 6.5 L7 5.4 L9 6 L9 8 Q5 9 2 5 Q1 3 2 1Z" fill="currentColor"/></svg>(555) 014-2280</li>
        <li><svg viewBox="0 0 10 10"><rect x="3" y="1" width="4" height="3" fill="currentColor"/><rect x="1" y="4" width="8" height="4" rx="1" fill="currentColor"/></svg>(555) 014-2281 fax</li>
        <li><svg viewBox="0 0 10 10"><rect x="1" y="2" width="8" height="6" fill="none" stroke="currentColor"/><path d="M1 2 L5 5.5 L9 2" fill="none" stroke="currentColor"/></svg>office@larkfieldledger.com</li>
        <li><svg viewBox="0 0 10 10"><circle cx="5" cy="5" r="4" fill="none" stroke="currentColor"/><path d="M1 5 H9 M5 1 Q2.5 5 5 9 M5 1 Q7.5 5 5 9" fill="none" stroke="currentColor" stroke-width="0.8"/></svg>www.larkfieldledger.com</li>
      </ul>
    </section>
    <section class="panel front-cover">
      <svg class="panel-art" width="480" height="640" viewBox="0 0 480 640">
        <path d="M0 0 H480 V365 Q180 345 0 215 Z" fill="var(--paper)"/>
        <path d="M480 365 Q180 345 0 215" fill="none" stroke="var(--brand-blue)" stroke-width="6"/>
      </svg>
      <span class="firm-name">Larkfield Ledger Partners</span>
    </section>
  </main>
</body>
</html>
```